Store Signage for New Location

I need a banner for my new location. It needs to communicate 1: our name, 2: our phone number 3: our message. This is going to be a 7 foot wide banner that is 4 feet tall. It needs to be a very high resolution design so it prints properly.

Our phone number is (913) 548-1907

Our Message: The HONEST alternative to the dealer.

Or: Your Honest Auto Service Center

"Honest" is our key word here.

Target Market(s)

Drive-by traffic.

Industry/Entity Type

Auto Repair

Requirements
Must have
• The name of our business: Tall Pine Auto Repair
• Our phone number: (913) 548-1907
• Our message: The HONEST alternative to the dealership.
• or: Your Honest Service Center
Nice to have
• I really just need a clean layout using the uploaded logo and font. It needs to be highly visible as a sign that is seen by drive-by traffic.
• I'd like the color scheme to be the same as what I have, however, you're more than welcome to add detail and color as needed.

```html
<!DOCTYPE html>
<html lang="en">
<head>
<meta charset="utf-8">
<title>Tall Pine Auto Repair — Store Banner</title>
<link href="https://fonts.googleapis.com/css2?family=Russo+One&display=swap" rel="stylesheet">
<style>
  :root {
    --stage: #e9ecef;
    --ink: #1b1b1d;
    --sky-light: #d3ecf9;
    --sky-deep: #7ed2f5;
    --brand-blue: #1b8fd0;
    --brand-orange: #f58a1f;
    --shop-grey: #9aa3ab;
    --shop-light: #d9dee2;
  }
  html, body {
    margin: 0;
    width: 1200px;
    height: 995px;
    overflow: hidden;
    background: var(--stage);
  }
  .canvas {
    position: relative;
    width: 1200px;
    height: 995px;
  }
  .banner {
    position: absolute;
    left: 40px;
    top: 178px;
    width: 1120px;
    height: 639px;
    display: block;
    box-shadow: 0 10px 30px rgba(0,0,0,.18);
  }
  .banner text {
    font-family: "Russo One", sans-serif;
    fill: var(--ink);
  }
</style>
</head>
<body>
<main class="canvas">
  <svg class="banner" viewBox="0 0 929 530" xmlns="http://www.w3.org/2000/svg" aria-labelledby="banner-title">
    <title id="banner-title">Tall Pine Auto Repair — The HONEST alternative to the dealer — (913) 548-1907</title>
    <defs>
      <linearGradient id="panel-fill" x1="0" y1="1" x2="1" y2="0">
        <stop offset="0" stop-color="var(--sky-light)"/>
        <stop offset="1" stop-color="var(--sky-deep)"/>
      </linearGradient>
      <linearGradient id="shop-fill" x1="0" y1="0" x2="0" y2="1">
        <stop offset="0" stop-color="var(--shop-light)"/>
        <stop offset="0.55" stop-color="var(--shop-grey)"/>
        <stop offset="1" stop-color="#c9ced2"/>
      </linearGradient>
    </defs>

    <!-- message panel -->
    <rect class="message-panel" x="0" y="0" width="929" height="530" fill="url(#panel-fill)"/>

    <!-- workshop photo area -->
    <polygon class="workshop-photo" role="img" aria-label="Photo of a repair shop bay with an SUV raised on a lift and a mechanic working beneath it"
      points="0,0 524,0 323,530 0,530" fill="url(#shop-fill)"/>

    <!-- accent bands -->
    <polygon class="divider-line" points="524,0 534,0 333,530 323,530" fill="var(--ink)"/>
    <polygon class="accent-orange" points="534,0 592,0 487,248 429,248" fill="var(--brand-orange)"/>
    <polygon class="accent-blue" points="450,234 509,234 383,530 326,530" fill="var(--brand-blue)"/>
    <polygon class="accent-blue-edge" points="509,234 519,234 393,530 383,530" fill="var(--ink)"/>

    <!-- business name -->
    <g class="brand-name">
      <circle cx="654" cy="68" r="9" fill="var(--ink)"/>
      <text x="876" y="73" text-anchor="end" font-size="14">Tall Pine Auto Repair</text>
    </g>

    <!-- message -->
    <text class="message-headline" x="876" y="272" text-anchor="end">
      <tspan font-size="21">The </tspan><tspan font-size="36">HONEST</tspan>
    </text>
    <text class="message-sub" x="876" y="299" text-anchor="end" font-size="18">alternative to the dealer</text>

    <!-- phone -->
    <g class="phone">
      <path class="phone-icon" fill="var(--ink)"
        d="M720,465 l4,-2 l4,6 l-3,2 c1,3 3,6 6,8 l2,-3 l6,3 l-2,4 c-8,1 -17,-9 -17,-18 z"/>
      <text x="876" y="482" text-anchor="end" font-size="15">(913) 548-1907</text>
    </g>
  </svg>
</main>
</body>
</html>
```